Construction Company

Design a clutter free business card, it can be double-sided utilizing the logo for BDN Ltd simple with all relevant contact information.

Please also a letterhead design to function for the purposes of invoicing, all mail requirements, with header to be distinctive while the footer ties page together and incorporates all necessary information.

For now, please use generic / dummy text and when a winner is selected, I will disclose the contact information.

Hi Designers! Please read the updated brief which includes the design of a business card and letterhead. Thank you!

```html
<!DOCTYPE html>
<html lang="en">
<head>
<meta charset="utf-8">
<title>BDN Ltd — Business Card</title>
<link rel="stylesheet" href="https://fonts.googleapis.com/css2?family=Cinzel:wght@400;600&display=swap">
<style>
  :root {
    --stage: #000000;
    --brand-blue: #243f8b;
    --brand-gold: #d4b22b;
    --paper: #f2f2f4;
  }
  * { margin: 0; padding: 0; box-sizing: border-box; }
  html, body {
    width: 1200px; height: 1200px; overflow: hidden;
    background: var(--stage);
  }
  .canvas { position: relative; width: 1200px; height: 1200px; }

  .card { position: absolute; left: 347px; width: 505px; height: 289px; overflow: hidden; }

  /* Front */
  .card--front { top: 266px; background: var(--paper); }
  .card--front .edge-bar {
    position: absolute; left: 0; top: 0; width: 13px; height: 100%;
    background: var(--brand-blue);
  }

  .wordmark {
    position: absolute; display: flex; align-items: baseline; gap: 4px;
    font-family: "Cinzel", serif; font-weight: 600; color: var(--brand-blue);
    white-space: nowrap;
  }
  .wordmark .name { font-size: 50px; line-height: 1; letter-spacing: -1px; }
  .wordmark .suffix { font-size: 13px; letter-spacing: 1px; }
  .wordmark .dot {
    align-self: center; width: 14px; height: 14px; border-radius: 50%;
    background: var(--brand-gold); margin-right: 6px;
  }
  .card--front .wordmark { left: 50%; top: 50%; transform: translate(-50%, -50%); }

  /* Back */
  .card--back { top: 644px; background: var(--brand-blue); }
  .card--back .edge-bar {
    position: absolute; right: 0; top: 0; width: 13px; height: 100%;
    background: var(--brand-gold);
  }
  .logo-panel {
    position: absolute; left: 0; top: 36px; width: 199px; height: 218px;
    background: var(--paper); border-radius: 0 44px 44px 0;
  }
  .card--back .wordmark { left: 14px; top: 50%; transform: translateY(-50%); }
  .card--back .wordmark .name { font-size: 44px; }
  .card--back .wordmark .suffix { font-size: 12px; }
  .card--back .wordmark .dot { width: 12px; height: 12px; margin-right: 4px; }

  .identity {
    position: absolute; left: 245px; top: 86px;
    font-family: "Cinzel", serif; color: var(--paper);
  }
  .identity .person { font-size: 19px; line-height: 1; letter-spacing: 0.5px; }
  .identity .role { font-size: 11px; letter-spacing: 2.2px; font-weight: 600; margin-top: 2px; }

  .contacts {
    position: absolute; left: 245px; top: 172px; list-style: none;
    font-family: "Cinzel", serif; color: var(--paper); font-size: 12px;
  }
  .contacts li { display: flex; align-items: center; height: 21.6px; }
  .contacts .icon {
    width: 16px; height: 16px; margin-right: 11px; flex: none;
    background: var(--brand-gold); display: flex; align-items: center; justify-content: center;
  }
  .contacts .icon svg { width: 12px; height: 12px; }
</style>
</head>
<body>
<main class="canvas">

  <section class="card card--front" aria-label="Business card front">
    <div class="edge-bar"></div>
    <div class="wordmark"><span class="dot"></span><span class="name">BDN</span><span class="suffix">LTD</span></div>
  </section>

  <section class="card card--back" aria-label="Business card back">
    <div class="logo-panel">
      <div class="wordmark"><span class="dot"></span><span class="name">BDN</span><span class="suffix">LTD</span></div>
    </div>

    <div class="identity">
      <p class="person">YOUR NAME</p>
      <p class="role">DESIGNATION</p>
    </div>

    <ul class="contacts">
      <li><span class="icon"><svg viewBox="0 0 12 12"><rect x="3.5" y="1" width="5" height="10" rx="1" fill="none" stroke="#243f8b" stroke-width="1.2"/><circle cx="6" cy="9.3" r="0.6" fill="#243f8b"/></svg></span>(000) 000-0000</li>
      <li><span class="icon"><svg viewBox="0 0 12 12"><path d="M2.5 1.5 L4.5 1.5 L5.3 4 L4 5 Q5 7.2 7 8 L8 6.7 L10.5 7.5 L10.5 9.5 Q10.5 10.5 9.5 10.5 Q2 10 1.5 2.5 Q1.5 1.5 2.5 1.5 Z" fill="#243f8b"/></svg></span>(000) 000-0000, (000) 000-0000</li>
      <li><span class="icon"><svg viewBox="0 0 12 12"><rect x="3" y="1" width="6" height="3" fill="#243f8b"/><rect x="1.5" y="4.5" width="9" height="4.5" rx="0.6" fill="#243f8b"/><rect x="3" y="8" width="6" height="3" fill="#d4b22b" stroke="#243f8b" stroke-width="0.8"/></svg></span>(000) 000-0000</li>
      <li><span class="icon"><svg viewBox="0 0 12 12"><rect x="1" y="2.5" width="10" height="7" fill="#243f8b"/><path d="M1.5 3 L6 6.5 L10.5 3" fill="none" stroke="#d4b22b" stroke-width="0.9"/></svg></span>ETC@YOUREMAIL.COM</li>
      <li><span class="icon"><svg viewBox="0 0 12 12"><circle cx="6" cy="6" r="4.6" fill="none" stroke="#243f8b" stroke-width="1"/><ellipse cx="6" cy="6" rx="2" ry="4.6" fill="none" stroke="#243f8b" stroke-width="0.8"/><path d="M1.4 6 H10.6" stroke="#243f8b" stroke-width="0.8"/></svg></span>WWW.YOURWEBSITE.COM</li>
    </ul>

    <div class="edge-bar"></div>
  </section>

</main>
</body>
</html>
```